Immobilienfirma sucht Flyerdesign
Zielgruppe
Wir sind ein Immobilienmaklerbüro spezialisiert auf den Verkauf von Einfamilienhäusern und Baugrundstücken im Umland von Berlin (Havelland & Oberhavel).
Zielgruppe des Flyers sind ausschließlich Eigentümer von Immobilien die verkaufen möchten.
Wir benötigen 6 - 8 Mal pro Jahre neue Flyer. Wir haben daher Interesse an einer regelmäßigen Zusammenarbeit.
Aufgabenstellung
Der Flyer soll im Format A 4 sein (hochkant).
Es soll eher Text sprechen, da wir möglichst viel Informationen transportieren möchten.
Wir richten uns ausschließlich an die Eigentümer (Verkäufer) von Immobilie die wir begeistern möchten gerade über uns zu verkaufen.
Unser Alleinstellungsmerkmal ist als "Makler OHNE Schilder" zu arbeiten, im Gegensatz zu unseren Mitbewerbern die die ganze Stadt zuplakatieren mit Werbebannern an Gartenzäunen und Straßenecken, Maklerschildern und Maklergalgen vor den zum Verkauf stehen Häusern etc.
Wir verkaufen diskret und bieten Verkäufern ein Komplettpaket von der unverbindlichen Erstberatung, über die kostenlose Wertermittlung, den kostenlosen Energieausweis, den kompletten Verkauf (natürlich ohne Schilder) bis zum Notartermin. Auch danach sind wir für den Verkäufer da und suchen ihm eine neue Bleibe und helfen auch mit Umzugsfirmen etc.
Komplettprogramm für Verkäufer - und selbstverständlich für Verkäufer komplett KOSTENLOS !
Als Bilder dachten wir an ein Portraitfoto von mir das mit Angebot ein Gesicht bekommt und der Kunde weiß wer ihm gegenüber sitzt, sowie ein eycatcher Bild.
Wir bieten unseren Kunden einen diskreten und schnellen Verkauf. Komplettservice : Kostenlose Wertermittlung, kostenloser Energieausweis, Übernahme des kompletten Verkaufs bis zum Notartermin, Hilfe bei der Suche nach neuer Immobilie, Hilfe beim Umzug.

```html
<!DOCTYPE html>
<html lang="de">
<head>
<meta charset="utf-8">
<title>Raumkontor West – Über uns</title>
<link href="https://fonts.googleapis.com/css2?family=Open+Sans:ital,wght@0,300;0,400;0,700;1,400&family=Arimo:ital@1&display=swap" rel="stylesheet">
<style>
  :root {
    --paper: #ffffff;
    --ink: #3b3b3b;
    --ink-soft: #4a4a4a;
    --accent-red: #8e0f0f;
    --rule: #8a8a8a;
    --wood-dark: #4f5a63;
    --wood-mid: #6d7880;
    --frame-light: #e9ecee;
  }
  * { margin: 0; padding: 0; box-sizing: border-box; }
  html, body { width: 1200px; height: 849px; overflow: hidden; background: var(--paper); }
  body { position: relative; font-family: "Open Sans", Arial, sans-serif; color: var(--ink); }

  .spread { position: relative; width: 1200px; height: 849px; }

  /* Left page: cover photo with claim */
  .cover-photo {
    position: absolute; left: 36px; top: 37px; width: 529px; height: 777px;
    background:
      radial-gradient(ellipse 60% 45% at 48% 42%, var(--frame-light) 0%, #b7c3d6 45%, rgba(0,0,0,0) 75%),
      radial-gradient(ellipse 35% 10% at 42% 71%, #d63a78 0%, rgba(0,0,0,0) 80%),
      linear-gradient(180deg, var(--wood-mid), var(--wood-dark));
  }
  .claim { position: absolute; left: 36px; top: 37px; width: 529px; height: 777px; color: #ffffff; font-weight: 300; }
  .claim span { position: absolute; white-space: nowrap; line-height: 1; }
  .claim .small { font-size: 20px; }
  .claim .big { font-size: 44px; letter-spacing: 0.5px; }
  .claim .der { left: 16px; top: 700px; }
  .claim .makler { left: 61px; top: 679px; }
  .claim .ohne { left: 53px; top: 719px; }
  .claim .schilder { left: 188px; top: 740px; }

  /* Right page */
  .page-header { position: absolute; left: 640px; top: 30px; width: 530px; height: 60px; }
  .page-header .header-rule { position: absolute; left: 76px; top: 26px; width: 268px; border-top: 1px solid var(--rule); }
  .brand { position: absolute; left: 352px; top: 16px; display: flex; align-items: center; gap: 7px; }
  .brand .brand-dot { width: 18px; height: 18px; border-radius: 50%; background: var(--ink-soft); }
  .brand .brand-name { font-size: 13px; font-weight: 400; color: var(--ink-soft); white-space: nowrap; }

  .about-title {
    position: absolute; left: 711px; top: 254px;
    font-size: 51px; font-weight: 700; letter-spacing: 1px; color: var(--ink); line-height: 1;
  }
  .about-lead {
    position: absolute; left: 700px; top: 314px; width: 123px;
    font-family: "Arimo", Arial, sans-serif; font-style: italic;
    font-size: 10px; line-height: 12.1px; text-align: right; color: var(--accent-red);
  }
  .about-divider { position: absolute; left: 831px; top: 317px; height: 310px; border-left: 1px solid var(--ink-soft); }
  .about-body {
    position: absolute; left: 841px; top: 314px; width: 260px;
    font-size: 10.4px; line-height: 12.1px; color: var(--ink-soft); hyphens: auto;
  }
  .about-body p + p { margin-top: 12.1px; }

  .page-footer { position: absolute; left: 637px; top: 808px; width: 530px; height: 14px; }
  .page-footer .footer-rule { position: absolute; left: 0; top: 6px; width: 481px; border-top: 1px solid var(--rule); }
  .page-footer .page-number { position: absolute; left: 486px; top: -1px; font-size: 10.5px; color: var(--ink); white-space: nowrap; }
</style>
</head>
<body>
<div class="spread">
  <div class="cover-photo" role="img" aria-label="Foto: weißes Sprossenfenster in grauer Holzfassade mit pinkem Blumenkasten voller bunter Blüten"></div>
  <div class="claim">
    <span class="small der">Der</span>
    <span class="big makler">MAKLER</span>
    <span class="big ohne">OHNE</span>
    <span class="small schilder">Schilder!</span>
  </div>

  <header class="page-header">
    <div class="header-rule"></div>
    <div class="brand"><span class="brand-dot"></span><span class="brand-name">Raumkontor West</span></div>
  </header>

  <h1 class="about-title">ÜBER UNS</h1>
  <p class="about-lead">Wir sind seit nunmehr 20 Jahren im Immobilienma&shy;nagement tätig. Wir haben zudem 6 Jahre Erfahrung im Immobilienvertrieb im Ausland gesammelt.</p>
  <div class="about-divider"></div>
  <div class="about-body" lang="de">
    <p>Wir sind seit nunmehr 20 Jahren im Immobilienmana&shy;gement tätig. Wir haben zudem 6 Jahre Erfahrung im Immobilienvertrieb im Ausland gesammelt. Wir haben umfassende Referenzen.</p>
    <p>Nun sind wir auf den Großraum Falkensee, Schönwal&shy;de - Glien, Dallgow - Döberitz, Brieselang, sowie Berlin Staaken und Berlin Spandau spezialisiert.</p>
    <p>In diesem Bereich verkaufen wir Einfamilienhäuser, vermieten Einfamilienhäuser, verkaufen Grundstü&shy;cke und verkaufen und vermieten Wohnungen sowie Gewerbeflächen.</p>
    <p>Wir abeiten hierbei sehr DISKRET (grundsätzliche KEI&shy;NE Verkaufsschilder auf Ihrem Grundstück) !</p>
    <p>Selbstverständlich ist unser Service für Eigentümer völlig kostenlos ! Keine Verkäuferprovisionen !</p>
    <p>Wir bieten Ihnen eine kostenfreie &amp; unverbindliche Wertermittlung Ihrer Immobilie, einen kostenlosen Energieausweis der für den Verkauf Ihrer Immobilie gesetzlich vorgeschrieben ist, kostenlose Einholung aller Genehmingungen etc. Wir bieten Ihnen den kom&shy;pletten Service aus einer Hand.</p>
  </div>

  <footer class="page-footer">
    <div class="footer-rule"></div>
    <span class="page-number">Seite 02</span>
  </footer>
</div>
</body>
</html>
```